QuillMark Business Cards

I need a business card designed for QuillMark. To get an idea of what we do please visit https://formvault.example/para-creadores-3

```html
<!DOCTYPE html>
<html lang="en">
<head>
<meta charset="utf-8">
<title>QuillMark Business Cards</title>
<link rel="stylesheet" href="https://fonts.googleapis.com/css2?family=Arimo:wght@400;700&display=swap">
<style>
  :root {
    --backdrop: #2b2c2e;
    --card-dark: #1c1e22;
    --card-amber: #e6941b;
    --amber: #f0a02a;
    --white: #ffffff;
    --rule: rgba(255,255,255,0.85);
  }
  * { box-sizing: border-box; margin: 0; padding: 0; }
  html, body {
    width: 1200px;
    height: 1015px;
    overflow: hidden;
    background: var(--backdrop);
    font-family: "Arimo", Arial, sans-serif;
  }
  .canvas {
    position: relative;
    width: 1200px;
    height: 1015px;
  }
  .card {
    position: absolute;
    width: 560px;
    height: 320px;
    box-shadow: 0 18px 40px rgba(0,0,0,0.55);
  }
  .card--front {
    left: 80px;
    top: 150px;
    background: var(--card-dark);
  }
  .card--back {
    left: 560px;
    top: 540px;
    background: var(--card-amber);
    color: var(--white);
  }
  .brand {
    position: absolute;
    left: 150px;
    top: 128px;
  }
  .brand__row {
    display: flex;
    align-items: center;
    gap: 18px;
  }
  .brand__square {
    width: 40px;
    height: 40px;
    border: 2px solid var(--amber);
  }
  .brand__name {
    color: var(--white);
    font-size: 30px;
    font-weight: 400;
    letter-spacing: 0.42em;
    text-transform: uppercase;
  }
  .brand__tagline {
    display: flex;
    align-items: center;
    gap: 12px;
    margin: 8px 0 0 58px;
  }
  .brand__tagline span {
    color: var(--amber);
    font-size: 9px;
    letter-spacing: 0.55em;
    text-transform: uppercase;
    white-space: nowrap;
  }
  .brand__tagline i {
    display: block;
    width: 110px;
    height: 1px;
    background: var(--rule);
  }
  .person {
    position: absolute;
    left: 48px;
    top: 60px;
  }
  .person__name {
    font-size: 20px;
    font-weight: 700;
    letter-spacing: 0.02em;
    text-transform: uppercase;
  }
  .person__role {
    font-size: 12px;
    letter-spacing: 0.04em;
    text-transform: uppercase;
    margin-top: 2px;
  }
  .contacts {
    list-style: none;
    margin-top: 26px;
  }
  .contacts li {
    display: flex;
    align-items: center;
    gap: 8px;
    font-size: 14px;
    line-height: 22px;
  }
  .contacts svg {
    width: 14px;
    height: 14px;
    flex: none;
  }
  .address {
    font-style: normal;
    font-size: 14px;
    line-height: 20px;
    margin-top: 28px;
  }
</style>
</head>
<body>
<main class="canvas">
  <section class="card card--front">
    <div class="brand">
      <div class="brand__row">
        <div class="brand__square"></div>
        <div class="brand__name">QuillMark</div>
      </div>
      <div class="brand__tagline"><span>Digital Notary</span><i></i></div>
    </div>
  </section>

  <section class="card card--back">
    <div class="person">
      <div class="person__name">Daniel Reyes</div>
      <div class="person__role">Managing Director</div>
      <ul class="contacts">
        <li>
          <svg viewBox="0 0 16 16" fill="none" stroke="#fff" stroke-width="1.6"><path d="M3 2h3l1 3-2 1.5a8 8 0 0 0 4.5 4.5L11 9l3 1v3a1 1 0 0 1-1 1A12 12 0 0 1 2 3a1 1 0 0 1 1-1z"/></svg>
          044-555 018 240
        </li>
        <li>
          <svg viewBox="0 0 16 16" fill="none" stroke="#fff" stroke-width="1.6"><rect x="1.5" y="3.5" width="13" height="9"/><path d="M1.5 3.5 8 9l6.5-5.5"/></svg>
          info@formvault.example
        </li>
        <li>
          <svg viewBox="0 0 16 16" fill="none" stroke="#fff" stroke-width="1.4"><circle cx="8" cy="8" r="6.5"/><ellipse cx="8" cy="8" rx="2.8" ry="6.5"/><path d="M1.5 8h13M2.5 5h11M2.5 11h11"/></svg>
          www.formvault.example
        </li>
      </ul>
      <address class="address">87, Harbor Lane Suite 4<br>20148, Eastmoor</address>
    </div>
  </section>
</main>
</body>
</html>
```